Attorney Website Design

I need a top quality attorney website layout designed. Here are some examples of what I feel are great websites:
http://www.quellmarstonseparationlaw.com/
http://www.vandriclegalgroup.com/
http://www.pobelaw.com/
http://www.harrowvaleaccusedcounselhq.com/
http://www.tzlegal.com/
http://www.brookhollowtrialjusticeoffice.com/
http://www.orvynchargedcounsel.com/
http://www.tzlegal.com/
What we like about these sites:
• The different layers
• Subtle designs, textures, curves
• 3 dimensional
• Floating effects
• Prominent phone number
• Location of Areas of Practice
• Request A Consultation Prominent
• Right side bar with practice areas
• Badges
• Clear Calls to Action
• Dynamic/Staying Top navigation when you scroll
The project will be for a home page and then also an interior page (should be similar to home page).
Updates
I want to make it understood I am looking for a design which is not a typical "template" site which I can find anywhere for $50. This budget and project is for a "Custom" website design. Please submit designs similar in quality to the samples links I have posted. Creativity is a MUST! The best way to explain this is, I want a design that I can feel it unique and original, not something that looks like 95% of all websites out there.
Neil
I just wanted everyone to know that so far I am not to pleased with any of the designs. I am not looking for cut/pasting of other peoples websites but ORIGINAL and CREATIVE work.
Reason: Weekend + Holiday extension.
Reason: Need more designs
Industry/Entity Type
Attorney

```html
<!DOCTYPE html>
<html lang="en">
<head>
<meta charset="utf-8">
<title>Ambervale Attorneys</title>
<link href="https://fonts.googleapis.com/css2?family=Anton&family=Open+Sans:ital,wght@0,400;0,600;0,700;1,400&family=Roboto:wght@400;500;700&display=swap" rel="stylesheet">
<style>
:root{
  --gold:#c8961a;
  --gold-dark:#a87a0c;
  --navy:#1f4f7e;
  --navy-dark:#2d4560;
  --footer:#3a5a7a;
  --ink:#2b2b2b;
  --body:#444;
  --panel:#efefef;
  --page:#f4f4f4;
  --white:#fff;
}
*{margin:0;padding:0;box-sizing:border-box}
html,body{width:978px;height:1200px;overflow:hidden}
body{position:relative;background:var(--page);font-family:"Open Sans",Arial,sans-serif;color:var(--body)}
.abs{position:absolute}

/* header */
.site-header{left:0;top:0;width:978px;height:88px;background:linear-gradient(#fff,#f6f6f6)}
.brand{left:106px;top:14px;font-size:29px;line-height:30px;font-weight:400;color:var(--gold)}
.brand span{display:block;color:var(--navy-dark)}
.btn-consult{left:536px;top:36px;width:162px;height:38px;border-radius:4px;background:linear-gradient(var(--gold),var(--gold-dark));color:#fff;font:600 14px/38px Roboto,sans-serif;text-align:center;box-shadow:2px 3px 4px rgba(0,0,0,.3)}
.phone{left:736px;top:44px;display:flex;align-items:center;gap:8px;font:700 17px Roboto,sans-serif;color:var(--navy)}

/* navigation */
.main-nav{left:0;top:88px;width:978px;height:38px;background:linear-gradient(#d8a82a,var(--gold-dark));border-top:1px solid #e6c46a}
.main-nav ul{list-style:none;display:flex;position:absolute;left:99px;top:0;height:38px}
.main-nav li{font:500 13px/38px Roboto,sans-serif;color:#fff;padding:0 9px}
.main-nav li.active{background:var(--navy-dark);padding:0 16px;margin-right:5px}

/* hero */
.hero{left:0;top:126px;width:978px;height:290px;background:linear-gradient(100deg,#8a8580 0%,#9fb4cf 35%,#5f86b8 55%,#dcdcd6 75%,#c9c7c0 100%)}
.hero-caption{left:0;top:236px;width:978px;height:50px;background:rgba(60,60,60,.55)}
.hero-title{left:118px;top:242px;font:31px/38px Anton,Impact,sans-serif;color:#fff;letter-spacing:.5px}
.btn-learn{left:754px;top:246px;width:119px;height:34px;background:linear-gradient(var(--gold),var(--gold-dark));color:#fff;font:500 13px/34px Roboto,sans-serif;text-align:center;box-shadow:1px 2px 3px rgba(0,0,0,.4)}
.hero-arrow{top:114px;width:30px;height:60px;background:rgba(255,255,255,.85)}
.hero-arrow.prev{left:0;border-radius:0 30px 30px 0}
.hero-arrow.next{right:0;border-radius:30px 0 0 30px}
.hero-arrow svg{position:absolute;top:22px}

/* welcome */
.welcome-title{left:117px;top:462px;font-size:20px;font-weight:600;color:var(--ink)}
.welcome-title b{color:var(--navy);font-weight:600}
.welcome-text{left:116px;top:498px;width:485px;font-size:11px;line-height:17px}
.welcome-text p{margin-bottom:13px}
.service{width:140px;text-align:center}
.service .disc{width:77px;height:77px;border-radius:50%;margin:0 auto;background:radial-gradient(circle at 50% 35%,#f2f2f2,#b8b8b8);display:flex;align-items:center;justify-content:center;box-shadow:0 1px 2px rgba(0,0,0,.2)}
.service h3{margin-top:7px;font:600 15px Roboto,sans-serif;color:var(--ink)}

/* media panel */
.media-panel{left:100px;top:760px;width:493px;height:221px;background:var(--panel)}
.media-divider{left:338px;top:775px;width:1px;height:190px;background:#d6d6d6;box-shadow:1px 0 0 #fff}
.panel-title{font-size:20px;font-weight:600;color:var(--ink)}
.panel-title b{color:var(--navy);font-weight:600}
.video-frame{left:112px;top:810px;width:204px;height:144px;background:#fff;border:1px solid #ddd;padding:4px}
.video-still{width:100%;height:120px;background:linear-gradient(135deg,#7a3a1a,#b86a2e 50%,#4a3a30)}
.video-bar{display:flex;align-items:center;gap:4px;height:13px;font-size:7px;color:#222;padding:0 3px;background:#e8e8e8}
.video-bar .track{flex:1;height:2px;background:#999}
.view-all{font:600 10px Roboto,sans-serif;color:var(--gold-dark)}
.testimonial .avatar{width:57px;height:47px;background:linear-gradient(#e6e6e6,#9ba4ad);border:2px solid #fff;box-shadow:0 0 2px rgba(0,0,0,.3)}
.testimonial q{position:absolute;left:65px;top:0;width:160px;font-size:10px;line-height:13.5px;color:#555;quotes:none}
.testimonial q::before{content:"\201C";font:700 17px Georgia,serif;color:#888;vertical-align:-4px;margin-right:2px}
.testimonial q::after{content:"\201D";font:700 17px Georgia,serif;color:#888;vertical-align:-9px;margin-left:4px}
.testimonial cite{position:absolute;left:145px;top:52px;font-style:normal;font-size:10px;color:#222}
.testimonial cite b{color:var(--navy);font-size:11px}

/* sidebar */
.sidebar{left:618px;top:463px;width:258px;height:519px;background:#fff;box-shadow:0 0 3px rgba(0,0,0,.2)}
.sidebar h2{position:absolute;left:27px;top:8px}
.practice-list{position:absolute;left:27px;top:40px;list-style:none}
.practice-list li{font:500 11px/21.7px Roboto,sans-serif;color:#222}
.practice-list li::before{content:"";display:inline-block;width:4px;height:4px;border-radius:50%;background:#888;margin-right:5px;vertical-align:2px}
.ask-box{position:absolute;left:14px;top:215px;width:230px;height:292px;background:var(--panel)}
.ask-title{position:absolute;left:17px;top:8px;font:italic 400 22px "Open Sans",sans-serif;color:var(--navy)}
.toll-free{position:absolute;left:19px;top:40px;font:italic 400 13px "Open Sans",sans-serif;color:var(--gold)}
.field{position:absolute;left:16px;width:202px;height:27px;background:#fff;border:1px solid #ccc;font-size:9px;color:#777;padding:7px 9px}
.btn-send{position:absolute;left:16px;top:247px;width:101px;height:27px;background:var(--navy-dark);color:#fff;font:500 13px/27px Roboto,sans-serif;text-align:center}

/* footer */
.footer-wave{left:0;top:930px;width:978px;height:270px}
.footer-col h4{font:500 13px Roboto,sans-serif;color:#fff;margin-bottom:10px}
.footer-col{color:#fff;font-size:10.5px}
.quick-links{list-style:none;line-height:14px}
.email-field{margin-top:10px;width:172px;height:22px;background:#fff;border:1px solid #ccc;font:italic 9.5px/20px "Open Sans",sans-serif;color:#444;padding-left:6px}
.btn-subscribe{margin-top:9px;width:94px;height:24px;background:linear-gradient(var(--gold),var(--gold-dark));font:700 12px/24px Roboto,sans-serif;text-align:center;box-shadow:1px 2px 3px rgba(0,0,0,.3)}
.contact-row{display:flex;gap:9px;align-items:flex-start;margin-bottom:9px;font-size:9.5px;line-height:12.5px}
.contact-row svg{flex:none;margin-top:1px}
.footer-brand{font-size:23px;line-height:27px;color:#fff}
.social{display:flex;gap:4px;margin-top:9px}
.social span{width:26px;height:26px;border-radius:50%;background:#fff}
.copyright{font-size:10px;line-height:15px;text-align:center;color:#fff}
</style>
</head>
<body>

<header class="site-header abs">
  <div class="brand abs">Ambervale<span>Attorneys</span></div>
  <div class="btn-consult abs">Request A Consultation</div>
  <div class="phone abs">
    <svg width="24" height="24" viewBox="0 0 24 24"><circle cx="12" cy="12" r="11" fill="none" stroke="#222" stroke-width="2"/><path d="M8.5 6.5l2 3-1.2 1.2c.8 1.7 2 2.9 3.8 3.8l1.2-1.2 3 2-1.3 1.8c-4.5-.5-8.5-4.5-9-9z" fill="#222"/></svg>
    123-456-7890
  </div>
</header>

<nav class="main-nav abs">
  <ul>
    <li class="active">Home</li>
    <li>Attorneys &amp; Staff</li>
    <li>Practice Areas</li>
    <li>Testimonials</li>
    <li>Video Center</li>
    <li>Free Consultation</li>
    <li>About Us</li>
    <li>Contact Us</li>
  </ul>
</nav>

<section class="hero abs" role="img" aria-label="Two smiling attorneys in front of a columned courthouse under a blue sky">
  <div class="hero-caption abs"></div>
  <div class="hero-title abs">ATTORNEYS YOU CAN TRUST</div>
  <div class="btn-learn abs">LEARN MORE</div>
  <div class="hero-arrow prev abs"><svg width="14" height="16" viewBox="0 0 14 16" style="left:6px"><path d="M10 2L4 8l6 6" fill="none" stroke="#333" stroke-width="2.5"/></svg></div>
  <div class="hero-arrow next abs"><svg width="14" height="16" viewBox="0 0 14 16" style="left:12px"><path d="M4 2l6 6-6 6" fill="none" stroke="#333" stroke-width="2.5"/></svg></div>
</section>

<h1 class="welcome-title abs">Welcome to <b>Ambervale Attorneys</b></h1>
<div class="welcome-text abs">
  <p>Lorem ipsum dolor sit amet, consectetuer adipiscing elit, sed diam nonummy nibh euismod tincidunt ut laoreet dolore magna aliquam erat volutpat. Ut wisi enim ad minim veniam, quis nostrud exerci tation ullamcorper suscipit lobortis nisl ut aliquip ex ea commodo consequat.</p>
  <p>Lorem ipsum dolor sit amet, consectetuer adipiscing elit, sed diam nonummy nibh euismod tincidunt ut laoreet dolore magna aliquam erat volutpat. Ut wisi enim ad minim...</p>
</div>

<div class="service abs" style="left:104px;top:616px">
  <div class="disc"><svg width="70" height="30" viewBox="0 0 70 30"><circle cx="17" cy="15" r="11" fill="none" stroke="#222" stroke-width="3"/><circle cx="53" cy="15" r="11" fill="none" stroke="#222" stroke-width="3"/><path d="M28 15h14" stroke="#222" stroke-width="2" stroke-dasharray="3 1.5"/></svg></div>
  <h3>Criminal Defense</h3>
</div>
<div class="service abs" style="left:284px;top:616px">
  <div class="disc"><svg width="54" height="44" viewBox="0 0 54 44"><g fill="#222"><circle cx="13" cy="6" r="5"/><path d="M6 13h14l4 16h-5v15h-4V33h-4v11h-4V29H3z"/><circle cx="41" cy="6" r="5"/><path d="M34 13h14v18h-3v13h-4V32h-2v12h-4V31h-1z"/><circle cx="27" cy="20" r="3.5"/><path d="M23 25h8v10h-2v9h-4v-9h-2z"/></g></svg></div>
  <h3>Family Law</h3>
</div>
<div class="service abs" style="left:457px;top:616px">
  <div class="disc"><svg width="36" height="44" viewBox="0 0 36 44"><g fill="#222"><circle cx="16" cy="8" r="7"/><path d="M4 18h24l4 26H0z"/></g><path d="M12 38l14-14 3 3-14 14H12z" fill="#fff"/></svg></div>
  <h3>Personal Injury</h3>
</div>

<section class="media-panel abs"></section>
<div class="media-divider abs"></div>
<h2 class="panel-title abs" style="left:117px;top:772px">Our <b>Video</b></h2>
<div class="video-frame abs">
  <div class="video-still" role="img" aria-label="Video still of attorneys meeting with a client in an office"></div>
  <div class="video-bar"><span>▶</span><span>00:00</span><span class="track"></span><span>00:00</span><span>◂▮▮</span></div>
</div>
<div class="view-all abs" style="left:259px;top:964px">View All &gt;&gt;</div>

<h2 class="panel-title abs" style="left:360px;top:775px">Client Testimonials</h2>
<div class="testimonial abs" style="left:362px;top:812px;width:226px;height:70px">
  <div class="avatar" role="img" aria-label="Client portrait"></div>
  <q>Lorem ipsum dol sit amet, This tetuer adipiscing elit, sed diam nonum sum ipsum</q>
  <cite><b>Lorem,</b> Director</cite>
</div>
<div class="testimonial abs" style="left:362px;top:890px;width:226px;height:70px">
  <div class="avatar" role="img" aria-label="Client portrait"></div>
  <q>Lorem ipsum dol sit amet, This tetuer adipiscing elit, sed diam nonum sum ipsum</q>
  <cite><b>Lorem,</b> Director</cite>
</div>
<div class="view-all abs" style="left:531px;top:964px">View All &gt;&gt;</div>

<aside class="sidebar abs">
  <h2 class="panel-title">Practice <b>Areas</b></h2>
  <ul class="practice-list">
    <li>DUI DEFENSE</li>
    <li>SERIOUS VEHICULAR CRIMES</li>
    <li>THEFT CRIMES</li>
    <li>DRUG CRIMES</li>
    <li>SEX CRIMES</li>
    <li>HIGH SCHOOL AND COLLEGE CASES</li>
    <li>OTHER OFFENSES</li>
    <li>EXPUNGEMENT</li>
  </ul>
  <div class="ask-box">
    <div class="ask-title">Ask Us Question?</div>
    <div class="toll-free">TOLL FREE : 1 (800) 555-0142</div>
    <div class="field" style="top:67px">Enter your Name</div>
    <div class="field" style="top:98px">Enter your Email Address</div>
    <div class="field" style="top:128px">Enter your Phone Number</div>
    <div class="field" style="top:159px;height:81px">Enter your Message</div>
    <div class="btn-send">SEND NOW</div>
  </div>
</aside>

<svg class="footer-wave abs" viewBox="0 0 978 270" preserveAspectRatio="none">
  <path d="M0 12 C110 85 250 110 420 106 C600 100 800 60 978 92 L978 100 C800 74 600 112 420 120 C250 126 100 112 0 66 Z" fill="#c8961a"/>
  <path d="M0 70 C100 114 250 130 420 124 C600 116 800 82 978 104 L978 270 L0 270 Z" fill="#3a5a7a"/>
</svg>

<div class="footer-col abs" style="left:116px;top:1048px">
  <h4>Quick Links</h4>
  <ul class="quick-links">
    <li>&gt; Home</li><li>&gt;Attorneys &amp; Staff</li><li>&gt; Practice Areas</li><li>&gt;Testimonials</li><li>&gt; Video Center</li><li>&gt; Free Consultation</li><li>&gt; About Us</li><li>&gt; Contact Us</li>
  </ul>
</div>

<div class="footer-col abs" style="left:269px;top:1050px">
  <h4>Subscribe to Newsletter</h4>
  <p style="line-height:16px;width:190px">get latest updates by entering your email address</p>
  <div class="email-field">Email Address</div>
  <div class="btn-subscribe">Subscribe</div>
</div>

<div class="footer-col abs" style="left:520px;top:1048px">
  <h4>Contact Us</h4>
  <div class="contact-row"><svg width="11" height="14" viewBox="0 0 11 14"><path d="M5.5 0A5.5 5.5 0 0 0 0 5.5C0 9 5.5 14 5.5 14S11 9 11 5.5A5.5 5.5 0 0 0 5.5 0z" fill="#ccd"/><circle cx="5.5" cy="5.5" r="2" fill="#3a5a7a"/></svg><span>Sreet Name, City Name<br>Zip Code-00000</span></div>
  <div class="contact-row"><svg width="11" height="11" viewBox="0 0 11 11"><rect x="0" y="3" width="11" height="6" fill="#ccd"/><rect x="2" y="0" width="7" height="4" fill="#ccd"/><rect x="2" y="7" width="7" height="4" fill="#ccd" stroke="#3a5a7a"/></svg><span>123-456-7890</span></div>
  <div class="contact-row"><svg width="11" height="11" viewBox="0 0 11 11"><path d="M1 0l3 3-1.5 1.5c1 2 2 3 4 4L8 7l3 3-1.5 1C4.5 10.5.5 6.5 0 1.5z" fill="#ccd"/></svg><span>123-456-7890</span></div>
  <div class="contact-row"><svg width="12" height="9" viewBox="0 0 12 9"><rect width="12" height="9" fill="#ccd"/><path d="M0 0l6 5 6-5" fill="none" stroke="#3a5a7a"/></svg><span>info@ambervalelaw.com</span></div>
</div>

<div class="footer-col abs" style="left:732px;top:1044px">
  <div class="footer-brand">Ambervale<br>Attorneys</div>
  <div class="social"><span></span><span></span><span></span><span></span></div>
</div>
<div class="copyright abs" style="left:690px;top:1141px;width:210px">Copyright 2014 AmbervaleAttorneys.<br>All reserved. Disclaimer</div>

</body>
</html>
```